Business card design for Automotive workshop

We need a business card for a new automotive repair and tyre shop called Ridgeback Prime Automotive located in New Zealand. We are a clean, modern and fresh workshop and company.

Front needs to feature logo,
my name:
Lachie Westergaard (director)

Address:
48 Marlow Lane
Tarrow Bay 3587

Phone: 07 842 1937
Mobile: 027 519 2764
Email: office@ridgebackmotors.co.nz
Website: ridgebackmotors.co.nz

Back needs to feature an area to write down appointment details, date and time.

Also feature a list of jobs and work we do such as,
Vehicle Servicing
All Mechanical Repairs
Warrant of Fitness
Tyres & Wheel Alignments
Automotive Diagnostics
Automotive Parts & Supplies

```html
<!DOCTYPE html>
<html lang="en">
<head>
<meta charset="utf-8">
<title>Ridgeback Prime Automotive – Business Card</title>
<link rel="stylesheet" href="https://fonts.googleapis.com/css2?family=Arimo:wght@400;700&family=Raleway:wght@700&display=swap">
<style>
  :root {
    --brand-red: #e41e26;
    --ink: #1a1a1a;
    --paper: #ffffff;
    --rule-grey: #d9d9d9;
    --backdrop: #ebe8e4;
  }
  * { margin: 0; padding: 0; box-sizing: border-box; }
  html, body { width: 1200px; height: 900px; overflow: hidden; }
  body {
    position: relative;
    background: var(--backdrop);
    font-family: "Arimo", Arial, sans-serif;
  }
  .card {
    position: absolute;
    left: 330px;
    width: 554px;
    height: 343px;
    overflow: hidden;
  }
  .card--front { top: 90px; background: var(--brand-red); color: var(--paper); }
  .card--back { top: 469px; background: var(--paper); }

  .abs { position: absolute; }
  .center { left: 0; width: 100%; text-align: center; }

  /* Front */
  .owner-name {
    top: 60px;
    font-family: "Raleway", Arial, sans-serif;
    font-weight: 700; font-size: 21px; letter-spacing: 0.3px;
  }
  .owner-role { top: 85px; font-size: 16px; }
  .contact-icons { top: 119px; left: 186px; }
  .contact-list { top: 153px; font-size: 16.5px; line-height: 20.3px; font-style: normal; }
  .contact-divider { top: 248px; left: 186px; width: 181px; height: 1px; background: rgba(255,255,255,0.75); }
  .contact-address { top: 261px; font-size: 16.5px; }

  /* Back */
  .brand-name {
    top: 61px;
    font-weight: 700; font-size: 28px; line-height: 36px; letter-spacing: 1px;
    color: var(--brand-red);
    display: flex; justify-content: center; align-items: center; gap: 10px;
  }
  .brand-mark { width: 13px; height: 13px; background: var(--ink); display: inline-block; }
  .appointment-heading {
    top: 144px;
    font-weight: 700; font-size: 18.5px; color: var(--brand-red);
  }
  .appointment-stripes { top: 146px; left: 30px; }
  .appointment-field { top: 190px; font-size: 18.5px; color: var(--ink); }
  .field-date { left: 98px; }
  .field-time { left: 290px; }
  .field-line { top: 201px; height: 1px; background: var(--rule-grey); }
  .line-date { left: 155px; width: 115px; }
  .line-time { left: 345px; width: 115px; }

  .services-band {
    left: 0; top: 237px; width: 100%; height: 106px;
    background: var(--brand-red);
  }
  .services-list {
    list-style: none; position: absolute; top: 13px;
    color: var(--paper); font-size: 16.5px; line-height: 25px;
  }
  .services-list li { padding-left: 15px; position: relative; }
  .services-list li::before {
    content: ""; position: absolute; left: 0; top: 8.5px;
    width: 9px; height: 9px; border-radius: 50%; background: var(--paper);
  }
  .services-list--left { left: 48px; }
  .services-list--right { left: 280px; }
</style>
</head>
<body>

<section class="card card--front" aria-label="Card front">
  <h1 class="abs center owner-name">LACHIE WESTERGAARD</h1>
  <p class="abs center owner-role">Director</p>

  <svg class="abs contact-icons" width="181" height="24" viewBox="0 0 181 24" aria-hidden="true">
    <line x1="0" y1="12" x2="45" y2="12" stroke="#fff" stroke-width="1"/>
    <line x1="136" y1="12" x2="181" y2="12" stroke="#fff" stroke-width="1"/>
    <g fill="#fff">
      <rect x="48" y="2" width="19" height="19" rx="4"/>
      <rect x="70" y="2" width="19" height="19" rx="4"/>
      <rect x="92" y="2" width="19" height="19" rx="4"/>
      <rect x="114" y="2" width="19" height="19" rx="4"/>
    </g>
    <g fill="#e41e26" stroke="#e41e26">
      <path d="M51.5 9.5 q6-4 12 0 v2 h-3 v-1.5 h-6 v1.5 h-3z" stroke="none"/>
      <rect x="53" y="12" width="9" height="5" rx="1" stroke="none"/>
      <rect x="76" y="5.5" width="7" height="12" rx="1.2" fill="none" stroke-width="1.6"/>
      <rect x="95.5" y="7" width="12" height="9" fill="none" stroke-width="1.5"/>
      <path d="M95.5 7 l6 5 l6 -5" fill="none" stroke-width="1.5"/>
      <circle cx="123.5" cy="11.5" r="5.5" fill="none" stroke-width="1.6"/>
      <path d="M118 11.5 h11 M123.5 6 v11" fill="none" stroke-width="1"/>
    </g>
  </svg>

  <address class="abs center contact-list">
    07 842 1937<br>
    027 519 2764<br>
    office@ridgebackmotors.co.nz<br>
    ridgebackmotors.co.nz
  </address>
  <div class="abs contact-divider"></div>
  <p class="abs center contact-address">48 Marlow Lane, Tarrow Bay 3587</p>
</section>

<section class="card card--back" aria-label="Card back">
  <div class="abs center brand-name"><span class="brand-mark"></span>RIDGEBACK PRIME</div>

  <svg class="abs appointment-stripes" width="497" height="16" viewBox="0 0 497 16" aria-hidden="true">
    <g fill="#1a1a1a">
      <polygon points="0,0 145,0 145,3 3,3"/>
      <polygon points="6,6 145,6 145,9 9,9"/>
      <polygon points="12,12 145,12 145,15 15,15"/>
      <polygon points="351,0 497,0 494,3 351,3"/>
      <polygon points="351,6 491,6 488,9 351,9"/>
      <polygon points="351,12 485,12 482,15 351,15"/>
    </g>
  </svg>
  <h2 class="abs center appointment-heading">NEXT APPOINTMENT</h2>

  <span class="abs appointment-field field-date">DATE</span>
  <div class="abs field-line line-date"></div>
  <span class="abs appointment-field field-time">TIME</span>
  <div class="abs field-line line-time"></div>

  <div class="abs services-band">
    <ul class="services-list services-list--left">
      <li>Vehicle Servicing</li>
      <li>All Mechanical Repairs</li>
      <li>Warrant of Fitness</li>
    </ul>
    <ul class="services-list services-list--right">
      <li>Tyres &amp; Wheel Alignments</li>
      <li>Automotive Diagnostics</li>
      <li>Automotive Parts &amp; Supplies</li>
    </ul>
  </div>
</section>

</body>
</html>
```